Women's Health Company needs business card

We need a business card for a USA based women's health care company. We use digital technology to enhance therapy prescribed by clinicians for their patients

```html
<!DOCTYPE html>
<html lang="en">
<head>
<meta charset="utf-8">
<title>Ondrava Health – Business Card</title>
<link rel="stylesheet" href="https://fonts.googleapis.com/css2?family=Montserrat:wght@400;500;600&display=swap">
<style>
  :root {
    --teal: #72bfbd;
    --purple: #8b519b;
    --ink: #222222;
    --paper: #ffffff;
    --backdrop: #e9e6e1;
  }
  * { margin: 0; padding: 0; box-sizing: border-box; }
  html, body { width: 900px; height: 1200px; overflow: hidden; }
  body {
    background: var(--backdrop);
    font-family: "Montserrat", Arial, sans-serif;
    color: var(--ink);
    position: relative;
  }
  .card {
    position: absolute;
    left: 80px;
    width: 742px;
    height: 442px;
    border-radius: 40px;
    box-shadow: 4px 6px 10px rgba(0,0,0,0.35);
  }
  .card--front { top: 130px; background: var(--paper); }
  .card--back { top: 637px; background: var(--purple); }

  .brand { position: absolute; color: var(--teal); font-weight: 500; line-height: 1; }
  .brand__name { display: block; }
  .brand__tag { display: block; text-transform: uppercase; }

  .card--front .brand { right: 52px; top: 66px; text-align: right; }
  .card--front .brand__name { font-size: 64px; letter-spacing: -1px; }
  .card--front .brand__tag { font-size: 27px; letter-spacing: 13px; margin-top: 10px; margin-right: -13px; }

  .card--back .brand { left: 0; right: 0; top: 136px; text-align: center; }
  .card--back .brand__name { font-size: 112px; letter-spacing: -2px; }
  .card--back .brand__tag { font-size: 44px; letter-spacing: 20px; margin-top: 22px; margin-right: -20px; }

  .person { position: absolute; left: 50px; top: 258px; }
  .person__name { color: var(--teal); font-size: 27px; font-weight: 600; line-height: 1.1; }
  .person__role { font-size: 16px; margin-top: 4px; }

  .divider {
    position: absolute;
    left: 48px; right: 48px; top: 314px;
    border-top: 1.5px solid var(--teal);
  }

  .contacts { position: absolute; left: 48px; top: 328px; list-style: none; }
  .contacts li { display: flex; align-items: center; font-size: 16px; height: 23.5px; }
  .contacts svg { width: 14px; height: 14px; margin-right: 12px; fill: var(--teal); }

  .address { position: absolute; left: 517px; top: 355px; font-size: 16px; line-height: 21px; font-style: normal; }
</style>
</head>
<body>
  <section class="card card--front">
    <div class="brand">
      <span class="brand__name">Ondrava</span>
      <span class="brand__tag">Health</span>
    </div>

    <div class="person">
      <h1 class="person__name">Clara Weiss</h1>
      <p class="person__role">Owner</p>
    </div>

    <div class="divider"></div>

    <ul class="contacts">
      <li>
        <svg viewBox="0 0 16 16" aria-hidden="true"><path d="M1 5c0-2 3-3 7-3s7 1 7 3v1h-4V4.5H5V6H1z M3 7h10l1 6H2z M8 8.5a2 2 0 1 0 0 4 2 2 0 0 0 0-4z"/></svg>
        +49 401 555 0182
      </li>
      <li>
        <svg viewBox="0 0 16 16" aria-hidden="true"><path d="M1 4h14v1L8 9.5 1 5z M1 6.5l7 4.5 7-4.5V13H1z"/></svg>
        info@ondravahealth.com
      </li>
      <li>
        <svg viewBox="0 0 16 16" aria-hidden="true"><path d="M8 1a7 7 0 1 0 0 14A7 7 0 0 0 8 1zm-1 2.5c1 0 2 1 1.5 2S7 7 6 7.5 4.5 9 5 10s0 2-1 2A5.5 5.5 0 0 1 7 3.5zm3 8c-1 0-1.5-1-1-2s2-1 2.5-2 1.5 0 1.5 1a5.5 5.5 0 0 1-3 3z"/></svg>
        www.ondravahealth.com
      </li>
    </ul>

    <address class="address">
      Quellenhofweg 31<br>
      20259 Hamburg
    </address>
  </section>

  <section class="card card--back">
    <div class="brand">
      <span class="brand__name">Ondrava</span>
      <span class="brand__tag">Health</span>
    </div>
  </section>
</body>
</html>
```